Electronic Music Artist needs an Album Cover

DRELL is an electronic musician from Boston, Massachusetts. He needs an album cover that captures the essence of his music. The album is called Waypoints, which represents his experiences growing up, positive and negative. He would like to see designs that involves color and creativity. Attached are some examples of artworks that DRELL likes. He also included a few of his original photos (optional to use. Using a photo will not effect his final decision!), and his logo.
Updates

Colors

Designer to choose colors to be used in the design.

Requirements
Must have
• My project must have the text "Waypoints" and "DRELL", and the logo (attached in the files). The logo should not be the main subject of the artwork. Everything must look aesthetically pleasing.
Nice to have
• It would be nice to have some sort of creative graphic design (see example album covers for reference). Also, in one of the references, there is a column on the left hand side with some text in it. That could be cool to include, but without the asian text.
Should not have
• The project should not have any other language besides English.

```html
<!DOCTYPE html>
<html lang="en">
<head>
<meta charset="utf-8">
<title>DRELL – Waypoints</title>
<link rel="stylesheet" href="https://fonts.googleapis.com/css2?family=Montserrat:wght@600;700&display=swap">
<style>
  :root {
    --stage: #e4e4e4;
    --ink: #0b0b0d;
    --white: #ffffff;
    --ember: #e2612a;
    --rust: #7a2a1e;
    --maroon: #3a1616;
    --gold: #b8894a;
    --sand: #d0a662;
    --lemon: #d9c94a;
    --violet: #5b3f6e;
    --mauve: #a07a92;
    --teal: #2fae8c;
  }
  * { box-sizing: border-box; margin: 0; padding: 0; }
  html, body {
    width: 845px;
    height: 1200px;
    overflow: hidden;
    background: var(--stage);
  }
  .canvas {
    position: relative;
    width: 845px;
    height: 1200px;
  }
  .album-cover {
    position: absolute;
    left: 32px;
    top: 210px;
    width: 780px;
    height: 780px;
    background: var(--ink);
    overflow: hidden;
    font-family: "Montserrat", Arial, sans-serif;
  }
  .collage-artwork {
    position: absolute;
    inset: 0;
    background:
      radial-gradient(ellipse 26% 34% at 50% 33%, rgba(217,201,74,.85), rgba(90,80,40,.55) 55%, transparent 75%),
      linear-gradient(180deg, transparent 0 10%, rgba(184,137,74,.9) 10% 60%, transparent 60%) 3% 0 / 36% 100% no-repeat,
      radial-gradient(ellipse 14% 40% at 82% 22%, rgba(160,122,146,.8), rgba(91,63,110,.5) 50%, transparent 80%),
      linear-gradient(90deg, var(--ember) 0, rgba(226,97,42,0) 6%),
      linear-gradient(180deg, var(--rust) 0%, var(--maroon) 28%, var(--ink) 70%);
  }
  .artist-mark {
    position: absolute;
    left: 413px;
    top: 118px;
    transform: translateX(-50%);
    display: flex;
    align-items: center;
    gap: 8px;
    color: var(--white);
    font-size: 22px;
    font-weight: 700;
    letter-spacing: .12em;
    line-height: 1;
  }
  .artist-mark .mark-square {
    width: 12px;
    height: 12px;
    background: var(--white);
  }
  .album-title {
    position: absolute;
    left: 286px;
    top: 279px;
    padding: 6px 18px 6px 20px;
    background: var(--ink);
    box-shadow: 10px 0 14px -6px var(--teal);
    color: var(--white);
    font-size: 28px;
    font-weight: 700;
    letter-spacing: .2em;
    line-height: 1.1;
  }
  .artist-name {
    position: absolute;
    left: 0;
    bottom: 0;
    width: 780px;
    height: 260px;
  }
  .artist-name text {
    font-family: "Montserrat", Arial, sans-serif;
    font-weight: 700;
    font-size: 215px;
    fill: var(--white);
  }
</style>
</head>
<body>
<main class="canvas">
  <section class="album-cover">
    <div class="collage-artwork" role="img" aria-label="Abstract photo collage: warm gold textured square, blurred leaf shadows, a dark torn shape streaked with yellow, violet light trails and a small fractal at the lower left"></div>

    <div class="artist-mark">
      <span class="mark-square"></span>
      <span class="mark-name">DRELL</span>
    </div>

    <h2 class="album-title">WAYPOINTS</h2>

    <svg class="artist-name" viewBox="0 0 780 260" aria-label="DRELL">
      <defs>
        <filter id="letter-outline" x="-5%" y="-10%" width="110%" height="120%">
          <feMorphology in="SourceAlpha" operator="erode" radius="4" result="inner"/>
          <feComposite in="SourceGraphic" in2="inner" operator="out"/>
        </filter>
      </defs>
      <text x="20" y="180" textLength="740" lengthAdjust="spacing" filter="url(#letter-outline)">DRELL</text>
    </svg>
  </section>
</main>
</body>
</html>
```